Pediatric Dental Practice needs a postcard for direct mail advertising

We are looking for a creative and professional double-sided postcard design for a direct mail marketing campaign. Our goal is to attract new families to our pediatric dental practice by conveying a sense of warmth, modern care, and clinical excellence. The design should feel "boutique" and high-end yet remain fun and approachable for parents and children.

```html
<!DOCTYPE html>
<html lang="en">
<head>
<meta charset="utf-8">
<title>Maple Grove Pediatric Dentistry – Postcard</title>
<link href="https://fonts.googleapis.com/css2?family=Cormorant+Garamond:wght@500;600&family=Montserrat:wght@400;500;600&display=swap" rel="stylesheet">
<style>
  :root{
    --bg:#f2f2f0;
    --cream:#faf8f4;
    --mint:#eef3ec;
    --green:#5fae66;
    --green-dark:#4e9a56;
    --green-soft:#cfe3cc;
    --ink:#333638;
    --ink-soft:#4a4d50;
    --rule:#d9dfd6;
    --white:#ffffff;
  }
  *{box-sizing:border-box;margin:0;padding:0}
  html,body{width:1200px;height:1022px;overflow:hidden;background:var(--bg)}
  body{position:relative;font-family:"Montserrat",sans-serif;color:var(--ink)}
  .serif{font-family:"Cormorant Garamond",serif}

  .card{position:absolute;left:96px;width:983px;overflow:hidden;box-shadow:0 6px 18px rgba(0,0,0,.18)}
  .card--front{top:87px;height:361px;background:var(--cream)}
  .card--back{top:537px;height:365px;display:flex}

  /* front */
  .front-photo{position:absolute;left:0;top:0;width:600px;height:100%;
    background:linear-gradient(90deg,#b9c4c9 0%,#d6d2d3 35%,#7fc3c7 62%,rgba(250,248,244,0) 100%)}
  .front-leaves{position:absolute;right:0;bottom:0;width:100px;height:200px;
    background:radial-gradient(ellipse at 60% 60%,rgba(207,227,204,.7),rgba(250,248,244,0) 70%)}
  .front-brand{position:absolute;left:520px;width:400px;top:18px;text-align:center}
  .brand-dot{display:block;width:56px;height:56px;border-radius:50%;background:var(--green-soft);margin:0 auto 14px}
  .brand-name{font-weight:500;color:var(--ink);line-height:1}
  .front-brand .brand-name{font-size:34px;letter-spacing:.5px}
  .front-brand .brand-sub{font-size:13px;letter-spacing:4px;margin-top:8px}
  .divider{display:block;width:26px;height:2px;background:var(--green);margin:0 auto}
  .front-brand .divider{margin-top:16px}
  .front-headline{font-size:26px;line-height:26px;color:var(--green);font-weight:500;margin-top:14px}
  .front-body{font-size:13.5px;line-height:19px;color:var(--ink-soft);margin-top:14px}
  .cta{display:inline-block;margin-top:14px;background:var(--green);color:var(--white);
    font-size:12px;letter-spacing:1.6px;font-weight:500;padding:6px 12px;border-radius:13px}

  /* back: features */
  .panel-features{width:379px;background:var(--mint);position:relative}
  .features-title{position:absolute;top:24px;width:100%;text-align:center;font-size:23px;color:var(--green);font-weight:500}
  .panel-features .divider{position:absolute;top:62px;left:176px}
  .feature-grid{position:absolute;left:18px;top:80px;width:344px;display:grid;grid-template-columns:repeat(3,1fr)}
  .feature{text-align:center;height:77px;border-right:1px solid var(--rule)}
  .feature:nth-child(3n){border-right:none}
  .feature:nth-child(-n+3){border-bottom:1px solid var(--rule);height:80px}
  .feature:nth-child(n+4){padding-top:10px;height:88px}
  .feature-icon{width:38px;height:38px;border-radius:50%;background:var(--green);margin:0 auto 6px;display:flex;align-items:center;justify-content:center}
  .feature-label{font-size:9.5px;line-height:12px;color:var(--ink-soft)}
  .goal{position:absolute;left:46px;top:255px;width:284px;height:86px;background:var(--white);border-radius:10px;text-align:center;padding-top:12px}
  .goal-title{font-size:16px;color:var(--green);font-weight:500}
  .goal-text{font-size:10.5px;line-height:15.5px;color:var(--ink);margin-top:6px}

  /* back: offer */
  .panel-offer{width:202px;position:relative;
    background:linear-gradient(180deg,#e6dccd 0%,#dcd8cf 35%,#cfccc3 60%,#ece8e0 80%,#dcb57a 100%)}
  .offer{position:absolute;left:17px;top:204px;width:165px;height:142px;background:var(--green);border-radius:9px;
    color:var(--white);text-align:center;padding-top:16px;box-shadow:0 2px 6px rgba(0,0,0,.15)}
  .offer-kicker{font-size:14px;letter-spacing:1.6px}
  .offer-amount{font-size:37px;line-height:38px;font-weight:600;margin-top:2px}
  .offer-sub{font-size:14px;margin-top:2px}
  .offer-fine{font-size:7px;line-height:11px;margin-top:12px;opacity:.95}

  /* back: mailing */
  .panel-mail{width:402px;background:var(--white);position:relative}
  .mail-brand{position:absolute;left:15px;top:24px}
  .mail-brand .brand-dot{width:30px;height:30px;margin:0 0 6px 24px}
  .mail-brand .brand-name{font-size:16px}
  .mail-brand .brand-sub{font-size:5.5px;letter-spacing:1.6px;margin-top:3px}
  .mail-address{position:absolute;left:15px;top:96px;font-size:9.5px;line-height:13.5px;color:var(--ink)}
  .postage{position:absolute;left:307px;top:22px;width:74px;height:79px;border:1px solid #777;text-align:center;
    font-size:8px;line-height:13px;padding-top:5px;color:var(--ink)}
  .postage strong{font-size:11px;font-weight:500}
  .mail-tagline{position:absolute;top:168px;width:360px;text-align:center;font-size:22px;line-height:23px;color:var(--green);font-weight:500}
  .panel-mail .divider{position:absolute;top:229px;left:167px}
  .mail-cta{position:absolute;top:238px;width:360px;text-align:center;font-size:12.5px;color:var(--ink)}
  .recipient{position:absolute;left:44px;top:291px;width:261px;height:51px;border:1px solid #cfcfcf;border-radius:4px;
    font-size:10px;padding:19px 0 0 24px;color:var(--ink)}
</style>
</head>
<body>

<section class="card card--front">
  <div class="front-photo" role="img" aria-label="Photo of a smiling young girl in a dental chair"></div>
  <div class="front-leaves" role="img" aria-label="Soft green leaf decoration"></div>
  <div class="front-brand">
    <span class="brand-dot"></span>
    <div class="brand-name">maple grove</div>
    <div class="brand-name brand-sub">PEDIATRIC DENTISTRY</div>
    <span class="divider"></span>
    <h1 class="front-headline serif">Gentle Care. Bright Futures.<br>Smiles for Life.</h1>
    <p class="front-body">Specialized dental care for children<br>in a warm, welcoming environment.</p>
    <span class="cta">NOW ACCEPTING NEW PATIENTS!</span>
  </div>
</section>

<section class="card card--back">
  <div class="panel-features">
    <h2 class="features-title serif">Where Little Smiles Thrive</h2>
    <span class="divider"></span>
    <div class="feature-grid">
      <div class="feature">
        <div class="feature-icon"><svg width="20" height="20" viewBox="0 0 20 20"><path d="M5 3c-3 0-3.5 4-2.5 6.5.6 1.5 1 3 1.3 5 .3 2.2 1.8 2.4 2.2.3.4-2 .8-3.3 4-3.3s3.6 1.3 4 3.3c.4 2.1 1.9 1.9 2.2-.3.3-2 .7-3.5 1.3-5C18.5 7 18 3 15 3c-2 0-3 1-5 1S7 3 5 3z" fill="none" stroke="#fff" stroke-width="1.6"/></svg></div>
        <div class="feature-label">Specialized<br>Pediatric Care</div>
      </div>
      <div class="feature">
        <div class="feature-icon"><svg width="20" height="20" viewBox="0 0 20 20"><path d="M10 17S2.5 12 2.5 7A3.8 3.8 0 0 1 10 5a3.8 3.8 0 0 1 7.5 2c0 5-7.5 10-7.5 10z" fill="none" stroke="#fff" stroke-width="1.7"/></svg></div>
        <div class="feature-label">Compassionate<br>&amp; Patient Team</div>
      </div>
      <div class="feature">
        <div class="feature-icon"><svg width="20" height="22" viewBox="0 0 20 22"><ellipse cx="10" cy="8" rx="5.5" ry="6.5" fill="#fff"/><path d="M10 14.5l-1 1.5h2zM10 16c-1 2 1 3 0 5" fill="none" stroke="#fff" stroke-width="1.2"/></svg></div>
        <div class="feature-label">Fun, Relaxing<br>Environment</div>
      </div>
      <div class="feature">
        <div class="feature-icon"><svg width="20" height="20" viewBox="0 0 20 20"><path d="M10 2l7 2.5v5c0 4-3 7-7 8.5C6 16.5 3 13.5 3 9.5v-5z" fill="none" stroke="#fff" stroke-width="1.7"/><path d="M10 2.5v15C6 16 3.5 13.3 3.5 9.5v-4.6z" fill="#fff"/></svg></div>
        <div class="feature-label">Preventive<br>&amp; Advanced Care</div>
      </div>
      <div class="feature">
        <div class="feature-icon"><svg width="20" height="20" viewBox="0 0 20 20"><rect x="3" y="4" width="14" height="13" rx="1.5" fill="none" stroke="#fff" stroke-width="1.6"/><path d="M3 8h14M7 2v4M13 2v4" stroke="#fff" stroke-width="1.6"/><g fill="#fff"><rect x="5.5" y="10" width="2" height="2"/><rect x="9" y="10" width="2" height="2"/><rect x="12.5" y="10" width="2" height="2"/><rect x="5.5" y="13.5" width="2" height="2"/><rect x="9" y="13.5" width="2" height="2"/></g></svg></div>
        <div class="feature-label">Convenient<br>Scheduling</div>
      </div>
      <div class="feature">
        <div class="feature-icon"><svg width="22" height="22" viewBox="0 0 22 22"><circle cx="11" cy="11" r="8" fill="none" stroke="#fff" stroke-width="1.6"/><circle cx="8" cy="9" r="1" fill="#fff"/><circle cx="14" cy="9" r="1" fill="#fff"/><path d="M7 12.5c1.8 3 6.2 3 8 0" fill="none" stroke="#fff" stroke-width="1.6"/></svg></div>
        <div class="feature-label">Positive<br>Dental Experiences</div>
      </div>
    </div>
    <div class="goal">
      <p class="goal-title serif">Our goal is simple:</p>
      <p class="goal-text">To help your child feel comfortable,<br>confident, and excited about their smile!</p>
    </div>
  </div>

  <div class="panel-offer" role="img" aria-label="Photo of the bright practice reception area with pendant light">
    <div class="offer">
      <p class="offer-kicker">SPECIAL OFFER!</p>
      <p class="offer-amount serif">$50 OFF</p>
      <p class="offer-sub serif">Your Child’s First Visit</p>
      <p class="offer-fine">New patients only. Not valid with<br>insurance or other offers. Expires 12/31/25.</p>
    </div>
  </div>

  <div class="panel-mail">
    <div class="mail-brand">
      <span class="brand-dot"></span>
      <div class="brand-name">maple grove</div>
      <div class="brand-name brand-sub">PEDIATRIC DENTISTRY</div>
    </div>
    <p class="mail-address">48 Bright Meadow Lane<br>Fairview, OH 44101</p>
    <div class="postage">PRSRT STD<br>ECRWSS<br>U.S. POSTAGE<br><strong>PAID</strong><br>EDDM RETAIL</div>
    <h2 class="mail-tagline serif">A lifetime of healthy<br>smiles starts here.</h2>
    <span class="divider"></span>
    <p class="mail-cta serif">Schedule your child’s appointment today!</p>
    <div class="recipient">Local Postal Customer</div>
  </div>
</section>

</body>
</html>
```